Design of a Web Development Agency

We're a web development agency (we do not offer design services). We'd like to get a new website up and running. We do custom web application development - large scale applications in the financial, healthcare, automotive, and other industries.

We need the following types of pages designed:
1) Homepage
2) Blog
3) Services page
4) Packages page
4) Generic content
5) Contact Us form.

The design should be consistent with our current icon. We're looking for a clean, corporate, brand. We'd like the design to expand on the concepts in the logo - the use of the electrical wiring motif / the colors / etc.

We offer the following services: 1) Corvel web hosting consulting, 2) custom application development, 3) eVN development, 4) Quillset development.

We offer packages in numbers of hours. We have about 3-4 tiers of services - the number of hours versus the monthly invoice total. For example, 5 hours per month of $500.00, for example.

Target Market(s)

Corporate clients

Industry/Entity Type

Electrical

Colors
acd036
33b7a4
33a6d7
3176b5
876aae
b768aa
fbee3e

Requirements
Must have
• Responsive / mobile friendly design.
• An email submitting form on the contact us page
Nice to have
• We'd like a bit of San Francisco to come through (where we're located)
• A plimbo map of our address on the contact us page
Should not have
• Excessive imagery. We don't have a lot of imagery, so we'd basically have to go out and find stock photography to put in it's place, which we just don't really want to do. All imagery should be supplied by the designer (we'll pay any copyright fees, if applicable, you just have to send us a list of the links to the imagery. Max budget would be $100-$200 on imagery, but preferably as little as possible).

```html
<!DOCTYPE html>
<html lang="en">
<head>
<meta charset="utf-8">
<title>Halden Web Works</title>
<link href="https://fonts.googleapis.com/css2?family=Oxygen:wght@300;400;700&family=Open+Sans:wght@400;600;700&display=swap" rel="stylesheet">
<style>
:root{
  --lime:#c8d92a;
  --lime-deep:#acd036;
  --lime-text:#b5c51c;
  --ink:#1c1c1c;
  --grey:#555;
  --muted:#8a8f5a;
  --line:#d9d9d9;
  --white:#fff;
  --night:#0b0b0b;
  --sky1:#2f6fb5;
  --sky2:#9cc4ea;
}
*{box-sizing:border-box;margin:0;padding:0}
html,body{width:972px;height:1200px;overflow:hidden;background:var(--white)}
body{font-family:"Oxygen",sans-serif;color:var(--ink);position:relative}
.abs{position:absolute}

/* header */
.topbar{left:0;top:0;width:972px;height:6px;background:#000}
.brand-mark{left:106px;top:18px;width:90px;height:90px;border:3px solid var(--ink);border-radius:50%;background:var(--lime)}
.brand-name{left:218px;top:50px;font-size:22px;font-weight:400;letter-spacing:.3px;color:var(--ink)}
.contact-line{top:26px;font-size:12px;font-weight:700;color:#333;display:flex;align-items:center;gap:6px}
.contact-line.email{left:596px}
.contact-line.phone{left:763px;font-size:15px;font-weight:400}
.follow{left:737px;top:60px;font-size:12px;font-weight:700;color:var(--lime-text);display:flex;align-items:center;gap:5px}
.social-dot{width:22px;height:22px;border-radius:50%;background:linear-gradient(#d8d8d8,#8d8d8d)}
.nav{left:433px;top:92px;display:flex;height:26px}
.nav a{display:block;height:26px;line-height:26px;background:#000;color:var(--white);font-size:11px;font-weight:700;text-decoration:none;text-align:center;border-left:2px solid var(--lime)}
.nav a.active{background:var(--lime);color:var(--ink);border-left:0}
.nav a.sep-blue{border-left-color:#33a6d7}
.header-rule{left:0;top:118px;width:972px;height:1px;background:#000}

/* hero */
.hero{left:0;top:119px;width:972px;height:361px;background:radial-gradient(ellipse at 78% 45%,#f0f5fb 0%,rgba(240,245,251,0) 35%),linear-gradient(180deg,var(--sky1) 0%,#6aa1d8 35%,var(--sky2) 70%,#5a87b8 100%)}
.hero-device{left:400px;top:180px;width:260px;height:290px;border-radius:30px;background:linear-gradient(160deg,#f2f2f2,#c9c9c9 60%,#b58e77)}
.hero-title{left:107px;top:232px;width:300px;font-size:28px;font-weight:700;line-height:36.5px;color:var(--white);text-shadow:0 1px 3px rgba(0,0,0,.35)}
.cta{left:104px;top:387px;width:178px;height:43px;background:var(--lime);border:1px solid #a7b71c;font-size:21px;color:var(--ink);display:flex;align-items:center;justify-content:center;letter-spacing:.3px}
.dots{left:104px;top:451px;display:flex;gap:5px}
.dots span{width:9px;height:9px;border-radius:50%;background:var(--white)}
.dots span.on{background:var(--lime)}

/* welcome */
.welcome-band{left:0;top:480px;width:972px;height:264px;background:linear-gradient(#ececec,#fff 40%,#f7f7f7)}
.welcome-kicker{left:106px;top:510px;font-size:15px;color:var(--lime-text)}
.welcome-brand{left:106px;top:532px;display:flex;align-items:center;gap:4px;font-size:20px}
.welcome-brand i{width:22px;height:22px;border:2px solid var(--ink);border-radius:50%;background:var(--lime)}
.welcome-rule{left:105px;top:565px;width:497px;height:1px;background:var(--line)}
.welcome-copy{left:105px;top:571px;width:498px;font-size:10.6px;line-height:15.9px;text-align:justify;color:#333}
.read-more{left:520px;top:702px;width:82px;text-align:right;font-size:11px;font-weight:700;color:var(--lime-text)}
.divider-v{left:622px;top:506px;width:1px;height:214px;background:var(--line)}
.quick{left:640px;top:505px;width:227px;height:216px;background:var(--white);border:1px solid #e2e2e2;box-shadow:0 6px 8px -4px rgba(0,0,0,.25)}
.quick h3{position:absolute;left:17px;top:10px;font-size:15px;font-weight:400;color:#333}
.quick h3 b{color:var(--lime-text);font-weight:400}
.quick .rule{position:absolute;left:15px;top:33px;width:195px;height:1px;background:var(--line)}
.field{position:absolute;left:16px;width:194px;height:21px;border:1px solid #cfcfcf;font-family:"Open Sans",sans-serif;font-size:9px;color:#999;padding:4px 6px}
.field.msg{height:51px}
.submit{position:absolute;left:16px;top:188px;width:61px;height:21px;background:var(--lime);border:1px solid #a7b71c;color:var(--white);font-family:"Open Sans",sans-serif;font-size:9px;font-weight:700;display:flex;align-items:center;justify-content:center;letter-spacing:.5px}

/* services */
.services{left:0;top:744px;width:972px;height:258px;background:repeating-linear-gradient(135deg,#cbdc26 0 2px,#c5d621 2px 4px)}
.services-title{left:0;top:765px;width:972px;text-align:center;font-size:22px;font-weight:700;letter-spacing:1px;color:var(--ink)}
.services-line{top:778px;width:180px;height:2px;background:linear-gradient(90deg,rgba(120,120,120,0),#8c8c8c)}
.services-line.right{transform:scaleX(-1)}
.service{top:816px;width:198px;text-align:center}
.service h4{font-size:11.5px;font-weight:400;line-height:14px;text-transform:uppercase;color:#5d6a10;height:30px}
.service.active h4{color:var(--ink);font-weight:700}
.service .disc{width:82px;height:82px;margin:5px auto 0;border-radius:50%;background:var(--white);border:3px solid #5a5a5a;display:flex;align-items:center;justify-content:center;box-shadow:0 8px 10px -6px rgba(0,0,0,.3)}
.service.active .disc{border-color:var(--ink)}
.service p{margin-top:14px;font-size:11px;line-height:15px;color:#6a7420}
.service.active p{color:var(--ink)}
.service-sep{top:820px;width:1px;height:150px;background:rgba(120,130,20,.35)}

/* footer */
.footer{left:0;top:1002px;width:972px;height:198px;background:linear-gradient(#262626,#000 60%)}
.foot-h{top:1019px;font-size:12.5px;font-weight:700;color:var(--lime)}
.foot-list{left:105px;top:1051px;list-style:none;font-size:10.5px;line-height:16px;color:var(--white)}
.foot-list li:first-child{font-weight:700}
.foot-sep{top:1022px;width:1px;height:128px;background:#333}
.post{left:274px;width:145px;font-size:10px;line-height:13.5px;color:var(--white)}
.post b{display:block;font-size:10.5px}
.post-rule{left:274px;top:1098px;width:140px;border-top:1px dashed #777}
.arrows{left:397px;top:1019px;color:var(--white);font-size:13px;font-weight:700;letter-spacing:2px}
.detail{left:508px;display:flex;gap:8px;align-items:flex-start;font-size:10.5px;line-height:13.5px;color:var(--white)}
.foot-mark{left:748px;top:1024px;width:118px;height:118px;border:2px solid #8a8a8a;border-radius:50%}
.foot-rule{left:105px;top:1168px;width:762px;height:1px;background:#2e2e2e}
.copyright{left:0;top:1179px;width:972px;text-align:center;font-size:10.5px;color:var(--white)}
</style>
</head>
<body>
<div class="abs topbar"></div>

<!-- header -->
<div class="abs brand-mark" aria-hidden="true"></div>
<div class="abs brand-name">HALDEN WEB WORKS</div>
<div class="abs contact-line email">
  <svg width="14" height="10" viewBox="0 0 14 10"><rect x=".5" y=".5" width="13" height="9" fill="none" stroke="#c8d92a"/><path d="M.5 .5 7 6l6.5-5.5" fill="none" stroke="#c8d92a"/></svg>
  info@haldenwebworks.com
</div>
<div class="abs contact-line phone">
  <svg width="15" height="15" viewBox="0 0 16 16"><circle cx="8" cy="8" r="7.3" fill="none" stroke="#c8d92a" stroke-width="1.2"/><path d="M5.5 4.5c-1 1.5 1 6 4 7l1-1.5-1.8-1-.8.8c-1-.6-1.8-1.8-2-2.8l.9-.6-.8-2z" fill="#c8d92a"/></svg>
  123.456.7890
</div>
<div class="abs follow">Follow Us On : <span class="social-dot"></span><span class="social-dot"></span></div>
<nav class="abs nav">
  <a class="active" style="width:62px">HOME</a>
  <a style="width:74px">SERVICES</a>
  <a style="width:78px">PACKAGES</a>
  <a style="width:78px">ABOUT US</a>
  <a style="width:52px">BLOG</a>
  <a class="sep-blue" style="width:90px">CONTACT US</a>
</nav>
<div class="abs header-rule"></div>

<!-- hero -->
<div class="abs hero" role="img" aria-label="Blurred bright office interior in blue tones"></div>
<div class="abs hero-device" role="img" aria-label="Hand holding a smartphone showing a colourful mobile site menu"></div>
<h1 class="abs hero-title">Lorem ipsum dolor sit amet nsectetuer adipiscing eli Lorem ipsum lorem</h1>
<div class="abs cta">GET STARTED</div>
<div class="abs dots"><span class="on"></span><span></span><span></span><span></span><span></span></div>

<!-- welcome -->
<div class="abs welcome-band"></div>
<div class="abs welcome-kicker">Welcome to</div>
<div class="abs welcome-brand"><i></i>HALDEN WEB WORKS</div>
<div class="abs welcome-rule"></div>
<p class="abs welcome-copy">Lorem ipsum dolor sit amet, consectetuer adipiscing elit, sed diam nonummy nibh euismod tincidunt ut laoreet dolore magna aliquam erat volutpat. Ut wisi enim ad minim veniam, quis nostrud exerci tation ullamcorper suscipit lobortis nisl ut aliquip ex ea commodo consequat. Duis autem vel eum iriure dolor in hendrerit in vulputate velit esse molestie consequat, vel illum dolore eu feugiat nulla facilisis at vero eros et accumsan et iusto odio dignissim qui blandit praesent luptatum zzril delenit augue duis dolore te feugait nulla facilisi. Duis autem vel eum iriure dolor in hendrerit in vulputate velit esse molestie consequat, vel illum dolore eu feugiat nulla facilisis at vero eros et accumsan et iusto odio dignissim qui blandit praesent luptatum zzril delenit augue duis dolore te feugait nulla facilisi.</p>
<div class="abs read-more">Read More »</div>
<div class="abs divider-v"></div>

<form class="abs quick">
  <h3><b>QUICK</b> CONTACT</h3>
  <div class="rule"></div>
  <div class="field" style="top:40px">Name</div>
  <div class="field" style="top:68px">Email</div>
  <div class="field" style="top:96px">Phone</div>
  <div class="field msg" style="top:124px">Message</div>
  <div class="submit">SUBMIT</div>
</form>

<!-- services -->
<section class="abs services"></section>
<div class="abs services-line" style="left:212px"></div>
<div class="abs services-line right" style="left:580px"></div>
<h2 class="abs services-title">OUR SERVICES</h2>

<div class="abs service active" style="left:88px">
  <h4>Corvel Web Hosting<br>Consulting</h4>
  <div class="disc">
    <svg width="44" height="40" viewBox="0 0 44 40"><rect x="4" y="4" width="36" height="24" fill="#c8d92a" stroke="#1c1c1c" stroke-width="2"/><rect x="18" y="28" width="8" height="6" fill="#1c1c1c"/><rect x="12" y="34" width="20" height="3" fill="#1c1c1c"/><path d="M12 10l8 8M12 10h5M12 10v5" stroke="#1c1c1c" stroke-width="2" fill="none"/><circle cx="29" cy="14" r="4" fill="#1c1c1c"/></svg>
  </div>
  <p>Lorem ipsum dolor sit,<br>consectetuedipiscing elit, sed</p>
</div>
<div class="abs service-sep" style="left:286px"></div>
<div class="abs service" style="left:287px">
  <h4>Custom Application<br>Development</h4>
  <div class="disc">
    <svg width="44" height="40" viewBox="0 0 44 40"><rect x="3" y="3" width="38" height="26" fill="#3a3a3a"/><rect x="6" y="6" width="32" height="20" fill="#fff"/><path d="M16 11l-5 5 5 5M28 11l5 5-5 5M24 10l-4 12" stroke="#3a3a3a" stroke-width="2" fill="none"/><rect x="18" y="29" width="8" height="6" fill="#3a3a3a"/><rect x="12" y="35" width="20" height="3" fill="#3a3a3a"/></svg>
  </div>
  <p>Lorem ipsum dolor sit,<br>consectetuedipiscing elit, sed</p>
</div>
<div class="abs service-sep" style="left:484px"></div>
<div class="abs service" style="left:485px">
  <h4>eVN<br>Development</h4>
  <div class="disc">
    <svg width="26" height="44" viewBox="0 0 26 44"><rect x="1" y="1" width="24" height="42" rx="4" fill="#3a3a3a"/><rect x="4" y="7" width="18" height="28" fill="#fff"/><circle cx="13" cy="39" r="2" fill="#fff"/></svg>
  </div>
  <p>Lorem ipsum dolor sit,<br>consectetuedipiscing elit, sed</p>
</div>
<div class="abs service-sep" style="left:682px"></div>
<div class="abs service" style="left:683px">
  <h4>Quillset<br>Development</h4>
  <div class="disc">
    <svg width="26" height="44" viewBox="0 0 26 44"><rect x="1" y="1" width="24" height="42" rx="4" fill="#3a3a3a"/><rect x="4" y="7" width="18" height="28" fill="#fff"/><circle cx="13" cy="39" r="2" fill="#fff"/></svg>
  </div>
  <p>Lorem ipsum dolor sit,<br>consectetuedipiscing elit, sed</p>
</div>

<!-- footer -->
<footer class="abs footer"></footer>
<h5 class="abs foot-h" style="left:105px">QUICK LINKS</h5>
<ul class="abs foot-list">
  <li>Home</li><li>Services</li><li>Packages</li><li>About Us</li><li>Blog</li><li>Contact Us</li>
</ul>
<div class="abs foot-sep" style="left:226px"></div>

<h5 class="abs foot-h" style="left:273px">BLOG POSTS</h5>
<div class="abs arrows">‹›</div>
<div class="abs post" style="top:1051px"><b>08/11/2014</b>Lorem ipsum dolor sit amet, cct etuer adipiscingin elit, sed diam</div>
<div class="abs post-rule"></div>
<div class="abs post" style="top:1104px"><b>09/11/2014</b>Lorem ipsum dolor sit amet, cct etuer adipiscingin elit, sed diam</div>
<div class="abs foot-sep" style="left:460px"></div>

<h5 class="abs foot-h" style="left:507px">CONTACT DETAILS</h5>
<div class="abs detail" style="top:1052px">
  <svg width="15" height="14" viewBox="0 0 15 14"><path d="M7.5 0 0 7h2v7h4V9h3v5h4V7h2z" fill="#fff"/></svg>
  <span>Lorem ipsum dolor sit amet,<br>adipiscing elit,</span>
</div>
<div class="abs detail" style="top:1096px">
  <svg width="15" height="15" viewBox="0 0 16 16"><circle cx="8" cy="8" r="7.2" fill="none" stroke="#fff" stroke-width="1.3"/><path d="M5.5 4.5c-1 1.5 1 6 4 7l1-1.5-1.8-1-.8.8c-1-.6-1.8-1.8-2-2.8l.9-.6-.8-2z" fill="#fff"/></svg>
  <span style="line-height:15px">123.456.7890</span>
</div>
<div class="abs detail" style="top:1128px">
  <svg width="15" height="15" viewBox="0 0 16 16"><text x="8" y="13" text-anchor="middle" font-size="15" font-weight="700" fill="#fff" font-family="Open Sans, sans-serif">@</text></svg>
  <span style="line-height:15px">info@haldenwebworks.com</span>
</div>
<div class="abs foot-sep" style="left:700px"></div>
<div class="abs foot-mark" aria-hidden="true"></div>

<div class="abs foot-rule"></div>
<div class="abs copyright">Copyright © 2014 &nbsp;Halden Web Works. All Rights Reserved</div>
</body>
</html>
```